Poster for the "Songs of the awakenings" concert

We need a poster for the concert: May 31, June 2 Songs of Awakenings.
In Program:Krallmeyer: Symphony No. 3 (Luminara)Veremintsky String Symphony No. 8Concert program exploring music that reflected milestone events of social change. Cantabili will present pieces that inspired or expressed progress, equality, human rights, and all human values we now take for granted.
Fri. May 31 / 8 pm / New Britain Hollowmere Meeting House Congregational (417 Pelham Ave)Sun. June 2 / 2 pm / Hartford Pellbrook Galleria Museum of Art (293 Ashgrove St)

Classical music audience, sophisticated

• Songs of Awakenings
• In Program:
• Krallmeyer: Symphony No. 3 (Luminara)
• Veremintsky String Symphony No. 8
• Dellan: Sinfonia Concertante for Violin and Viola
• Ilvana Dreskoli, violin, Tobias Marrend, viola, conductor
• Concert program exploring music that reflected milestone events of social change.
• Cantabili will present pieces that inspired or expressed progress, equality, human rights.
• Fri. May 31 / 8 pm / New Britain
• Hollowmere Meeting House Congregational (417 Pelham Ave)
• Sun. June 2 / 2 pm / Hartford
• Pellbrook Galleria Museum of Art (293 Ashgrove St)
• www.thecantabili-example.org
• Phone: (555) 014-KLMB (5562)

```html
<!DOCTYPE html>
<html lang="en">
<head>
<meta charset="utf-8">
<title>Songs of Awakenings — Concert Poster</title>
<link rel="stylesheet" href="https://fonts.googleapis.com/css2?family=League+Spartan:wght@700;800;900&family=Montserrat:wght@300;400&display=swap">
<style>
  :root {
    --orange: #fbab4c;
    --charcoal: #2f2f2f;
    --umber: #7a5636;
    --paper: #efdcb4;
    --paper-deep: #d9bf8c;
    --white: #ffffff;
  }
  html, body {
    margin: 0;
    padding: 0;
    overflow: hidden;
    background: var(--orange);
  }
  .poster {
    position: relative;
    width: 848px;
    height: 1200px;
    overflow: hidden;
    background: var(--orange);
    font-family: "League Spartan", "Montserrat", sans-serif;
    color: var(--white);
  }
  .backdrop {
    position: absolute;
    inset: 0;
    width: 848px;
    height: 1200px;
  }
  .program {
    position: absolute;
    left: 112px;
    right: 0;
    top: 58px;
    text-align: center;
  }
  .program-heading {
    margin: 0 0 18px;
    font-weight: 800;
    font-size: 44px;
    line-height: 1;
    letter-spacing: 0.5px;
    text-transform: uppercase;
  }
  .program-list {
    list-style: none;
    margin: 0;
    padding: 0;
    font-weight: 800;
    font-size: 16.5px;
    text-transform: uppercase;
  }
  .program-list li { line-height: 32px; }
  .program-note {
    margin: 12px 0 0;
    font-family: "Montserrat", sans-serif;
    font-weight: 400;
    font-size: 20.5px;
    line-height: 25px;
  }
  .program-note + .program-note { margin-top: 12px; }
  .title {
    position: absolute;
    left: 28px;
    top: 470px;
    margin: 0;
    font-weight: 900;
    font-size: 124px;
    line-height: 88px;
    letter-spacing: -3px;
    text-transform: uppercase;
  }
  .score-sheet {
    position: absolute;
    left: 282px;
    top: 694px;
    width: 300px;
    height: 210px;
    transform: rotate(9deg);
    background: linear-gradient(135deg, var(--paper), var(--paper-deep));
  }
  .performance {
    position: absolute;
    left: 30px;
    text-transform: uppercase;
  }
  .performance.friday { top: 770px; }
  .performance.sunday { top: 982px; left: 26px; }
  .performance-when {
    margin: 0;
    font-weight: 800;
    font-size: 46px;
    line-height: 50px;
  }
  .performance-venue {
    margin: 4px 0 0;
    font-weight: 800;
    font-size: 16px;
    line-height: 19px;
  }
  .contact {
    position: absolute;
    right: 32px;
    top: 1106px;
    text-align: right;
    font-weight: 800;
    font-size: 16px;
    line-height: 21px;
    text-transform: uppercase;
  }
</style>
</head>
<body>
<main class="poster">
  <svg class="backdrop" viewBox="0 0 848 1200" aria-hidden="false">
    <defs>
      <linearGradient id="crowd-tone" x1="0" y1="0" x2="1" y2="0">
        <stop offset="0" stop-color="#7a5636"/>
        <stop offset="0.2" stop-color="#2f2f2f"/>
        <stop offset="0.45" stop-color="#5b4332"/>
        <stop offset="0.7" stop-color="#2f2f2f"/>
        <stop offset="1" stop-color="#7a5636"/>
      </linearGradient>
    </defs>
    <polygon class="banner" points="88,0 290,0 848,48 848,372 112,384" fill="var(--charcoal)"/>
    <path class="crowd" role="img" aria-label="Silhouetted crowd of marchers holding up a banner"
          d="M0,400 L112,384 L848,372 L848,1200 L0,1200 Z" fill="url(#crowd-tone)"/>
  </svg>

  <section class="program">
    <h2 class="program-heading">In Program</h2>
    <ul class="program-list">
      <li>Krallmeyer: Symphony No. 3 (Luminara)</li>
      <li>Veremintsky String Symphony No. 8</li>
      <li>Dellan: Sinfonia Concertante for Violin and Viola</li>
    </ul>
    <p class="program-note">Concert program exploring music<br>that reflected milestone events of social change</p>
    <p class="program-note">Cantabili will present pieces that inspired or expressed<br>progress, equality, human rights</p>
  </section>

  <h1 class="title">Songs of<br>Awakenings</h1>

  <div class="score-sheet" role="img" aria-label="Handwritten sheet of musical score"></div>

  <section class="performance friday">
    <p class="performance-when">Fri. May 31<br>8 pm<br>New Britain</p>
    <p class="performance-venue">Hollowmere Meeting House Congregational<br>(417 Pelham Ave)</p>
  </section>

  <section class="performance sunday">
    <p class="performance-when">Sun. June 2<br>2 pm<br>Hartford</p>
    <p class="performance-venue">Pellbrook Galleria Museum of Art<br>(293 Ashgrove St)</p>
  </section>

  <footer class="contact">
    www.thecantabili-example.org<br>
    Phone: (555) 014-KLMB (5562)
  </footer>
</main>
</body>
</html>
```